Stationery Design Project - Tarnwell Corporate

Business Cards
Size: 90mm x 55mm
Letterhead
Size: A4 - 210mm x 297mm
With Compliments Slip
Size: DL - 210mm x 99mm
Presentation Folder
Size: A4

Tarnwell Corporate
website: www.tarnwellcorporate.com.au (Under construction)
Offices: *Kestrel Bay *Ashford Vale * Norhaven

A company that supply Safety consultantcy services

```html
<!DOCTYPE html>
<html lang="en">
<head>
<meta charset="utf-8">
<title>Tarnwell Corporate – Presentation Folder</title>
<link rel="stylesheet" href="https://fonts.googleapis.com/css2?family=Questrial&display=swap">
<style>
  :root {
    --backdrop: #d9d9d9;
    --paper: #ffffff;
    --navy: #1f3f78;
    --royal: #0f5a9a;
    --sky: #4e9fd0;
    --steel: #9a9ea4;
    --ink: #1c1c1c;
    --brand-blue: #1a6fae;
  }
  * { box-sizing: border-box; margin: 0; padding: 0; }
  html, body {
    width: 1200px; height: 900px; overflow: hidden;
    background: var(--backdrop);
    font-family: "Questrial", "Century Gothic", sans-serif;
  }
  .canvas { position: relative; width: 1200px; height: 900px; }

  .folder-face {
    position: absolute; top: 75px; width: 520px; height: 740px;
    box-shadow: 0 6px 18px rgba(0,0,0,.25);
    overflow: hidden;
  }
  .folder-front { left: 50px; background: var(--paper); }
  .folder-back { left: 630px; }

  .brand {
    position: absolute; top: 330px; left: 0; right: 0;
    display: flex; align-items: center; justify-content: center; gap: 14px;
  }
  .brand-square { width: 26px; height: 26px; background: var(--brand-blue); }
  .brand-name {
    font-size: 40px; color: var(--brand-blue); letter-spacing: 1px;
  }

  .front-band { position: absolute; left: 0; bottom: 0; width: 520px; height: 210px; }

  .office-list {
    position: absolute; left: 0; right: 0; bottom: 50px;
    text-align: center; color: #fff; font-size: 19px; letter-spacing: .5px;
  }
  .office-list .sep {
    display: inline-block; width: 6px; height: 6px; background: #fff;
    vertical-align: middle; margin: 0 10px;
  }

  .back-artwork { position: absolute; inset: 0; }

  .contact-block {
    position: absolute; left: 0; right: 0; bottom: 32px;
    color: #fff; font-size: 9.5px; font-style: normal;
    text-align: center; line-height: 1.6; letter-spacing: .3px;
  }
  .contact-block .row { display: flex; justify-content: center; gap: 14px; align-items: center; }
  .contact-block svg { width: 9px; height: 9px; vertical-align: -1px; margin-right: 3px; fill: #fff; }
</style>
</head>
<body>
<main class="canvas">

  <section class="folder-face folder-front" aria-label="Presentation folder front cover">
    <div class="brand">
      <span class="brand-square"></span>
      <span class="brand-name">Tarnwell Corporate</span>
    </div>

    <svg class="front-band" viewBox="0 0 520 210" preserveAspectRatio="none">
      <defs>
        <linearGradient id="bandSteel" x1="0" x2="1" y1="0" y2="0">
          <stop offset="0" stop-color="#8e9196"/>
          <stop offset=".45" stop-color="#dfe2e6"/>
          <stop offset=".6" stop-color="#9cc7e6"/>
          <stop offset="1" stop-color="#0f5a9a"/>
        </linearGradient>
        <linearGradient id="bandDeep" x1="0" x2="1" y1="0" y2="1">
          <stop offset="0" stop-color="#1d3b73"/>
          <stop offset=".7" stop-color="#24508d"/>
          <stop offset="1" stop-color="#2a6aa8"/>
        </linearGradient>
      </defs>
      <polygon points="0,20 220,55 520,0 520,90 0,90" fill="url(#bandSteel)"/>
      <rect x="0" y="60" width="520" height="150" fill="url(#bandDeep)"
            role="img" aria-label="Abstract blue 3D block artwork"/>
      <polygon points="0,20 220,55 520,0 520,8 220,62 0,60" fill="url(#bandSteel)"/>
    </svg>

    <p class="office-list">Kestrel Bay<span class="sep"></span>Ashford Vale<span class="sep"></span>Norhaven</p>
  </section>

  <section class="folder-face folder-back" aria-label="Presentation folder back cover">
    <svg class="back-artwork" viewBox="0 0 520 740" preserveAspectRatio="none"
         role="img" aria-label="Abstract blue 3D block artwork filling the back cover">
      <defs>
        <linearGradient id="backDeep" x1="0" x2="1" y1="0" y2="1">
          <stop offset="0" stop-color="#1c3c74"/>
          <stop offset=".55" stop-color="#214c88"/>
          <stop offset="1" stop-color="#3f8cc4"/>
        </linearGradient>
      </defs>
      <rect width="520" height="740" fill="url(#backDeep)"/>
    </svg>

    <address class="contact-block">
      <div class="row">
        <span><svg viewBox="0 0 10 10"><path d="M5 0a3.5 3.5 0 0 0-3.5 3.5C1.5 6 5 10 5 10s3.5-4 3.5-6.5A3.5 3.5 0 0 0 5 0zm0 5a1.5 1.5 0 1 1 0-3 1.5 1.5 0 0 1 0 3z"/></svg>42 Larkspur Road Elmsford, Westmark</span>
      </div>
      <div class="row">
        <span><svg viewBox="0 0 10 10"><circle cx="5" cy="5" r="5"/></svg>www.tarnwellcorporate.com.au</span>
        <span><svg viewBox="0 0 10 10"><path d="M2 0l2 2.5-1.2 1.3a6 6 0 0 0 3.4 3.4L7.5 6 10 8l-1.5 2C4 10 0 6 0 1.5z"/></svg>08 6100 2233</span>
        <span><svg viewBox="0 0 10 10"><rect x="1" y="3" width="8" height="5"/><rect x="2.5" y="0" width="5" height="3"/></svg>08 6100 2244</span>
      </div>
    </address>
  </section>

</main>
</body>
</html>
```